Owner
Vireltex Golf Cart Cushion Covers
Bright & Fun-filled
Maelys Brant
348 Heron Mill Lane
Stamford, CT
maelysbrant@snugwraps.example
snugwraps.example
Snug Wraps are golf cart cushion covers made out of Vireltex Fleece. They are made in the USA.
Vireltex fleece golf cart cushion covers
available with custom embroidery

```html
<!DOCTYPE html>
<html lang="en">
<head>
<meta charset="utf-8">
<title>Snug Wraps Stationery</title>
<link href="https://fonts.googleapis.com/css2?family=Open+Sans:wght@400;600;800&display=swap" rel="stylesheet">
<style>
  :root{
    --bg:#e9e7e4;
    --paper:#ffffff;
    --ink:#3a3a3a;
    --muted:#8a8a8a;
    --dark:#1d1d1f;
    --brand:#2b2f8f;
    --line:#cfcfcf;
    --band-top:#2a2a30;
  }
  *{box-sizing:border-box;margin:0;padding:0}
  html,body{width:1200px;height:552px;overflow:hidden}
  body{background:var(--bg);font-family:"Open Sans",Arial,sans-serif;color:var(--ink);position:relative}
  .sheet{position:absolute;background:var(--paper);box-shadow:0 3px 10px rgba(0,0,0,.25);overflow:hidden}
  .wordmark{display:flex;align-items:center;gap:6px;font-weight:800;color:var(--brand);white-space:nowrap}
  .wordmark .dot{border-radius:50%;background:var(--brand);flex:none}
  .footer-band{position:absolute;left:0;right:0;bottom:0;background:linear-gradient(180deg,var(--band-top),var(--dark))}
  .band-text{position:absolute;left:14px;bottom:8px;color:#fff;z-index:2}
  .band-text-right{position:absolute;right:14px;bottom:8px;color:#fff;text-align:right;z-index:2}

  /* business card */
  .business-card{left:66px;top:20px;width:246px;height:148px}
  .business-card .holder{position:absolute;left:14px;top:12px;font-size:10px;font-weight:600}
  .business-card .contact{position:absolute;left:14px;top:32px;font-size:5.5px;line-height:8.5px;color:var(--muted)}
  .business-card .wordmark{position:absolute;right:14px;top:40px;font-size:13px}
  .business-card .wordmark .dot{width:10px;height:10px}
  .business-card .footer-band{height:36px}
  .business-card .band-text{font-size:5px;line-height:7px}

  /* envelopes */
  .envelope-back{left:66px;top:186px;width:282px;height:150px;background:var(--dark)}
  .envelope-back .flap{position:absolute;inset:0;width:100%;height:100%}
  .envelope-back .wordmark{position:absolute;left:50%;top:40px;transform:translateX(-50%);font-size:13px;color:#fff}
  .envelope-back .wordmark .dot{width:10px;height:10px;background:#fff}
  .envelope-front{left:66px;top:340px;width:282px;height:148px}
  .envelope-front .wordmark{position:absolute;left:14px;top:14px;font-size:12px}
  .envelope-front .wordmark .dot{width:9px;height:9px}
  .envelope-front .return{position:absolute;left:14px;top:34px;font-size:5px;line-height:7px;color:var(--muted)}
  .envelope-front .footer-band{height:34px}
  .envelope-front .band-text{font-size:5px;line-height:7px}

  /* letterhead */
  .letterhead{left:448px;top:20px;width:290px;height:512px}
  .letterhead .wordmark{position:absolute;left:50%;top:28px;transform:translateX(-50%);font-size:14px}
  .letterhead .wordmark .dot{width:11px;height:11px}
  .letter-body{position:absolute;left:24px;right:24px;top:72px;font-size:5.3px;line-height:8.5px;color:#555}
  .letter-body p{margin-bottom:7px}
  .letterhead .footer-band,.fax-sheet .footer-band{height:44px}
  .letterhead .band-text,.letterhead .band-text-right,
  .fax-sheet .band-text,.fax-sheet .band-text-right{font-size:5px;line-height:7px;bottom:12px}

  /* fax */
  .fax-sheet{left:790px;top:56px;width:340px;height:476px}
  .fax-sheet .wordmark{position:absolute;left:50%;top:24px;transform:translateX(-50%);font-size:14px}
  .fax-sheet .wordmark .dot{width:11px;height:11px}
  .fax-title{position:absolute;right:30px;top:62px;font-size:14px;font-weight:800;letter-spacing:1px;color:var(--ink)}
  .fax-fields{position:absolute;left:24px;right:24px;top:88px;display:grid;grid-template-columns:1fr 1fr;column-gap:18px;row-gap:9px}
  .fax-field{display:flex;align-items:flex-end;gap:6px;font-size:5.5px;color:var(--ink)}
  .fax-field span{flex:1;border-bottom:1px solid var(--line);height:8px}
  .fax-checks{position:absolute;left:24px;right:24px;top:148px;display:flex;justify-content:space-between;font-size:5px}
  .fax-checks label{display:flex;align-items:center;gap:3px}
  .fax-checks i{width:6px;height:6px;border:1px solid var(--muted);display:inline-block}
  .fax-comments{position:absolute;left:24px;right:24px;top:164px;font-size:5.5px;font-weight:600;border-top:1px solid var(--line);padding-top:5px}
</style>
</head>
<body>

<section class="sheet business-card">
  <div class="holder">Maelys Brant</div>
  <div class="contact">
    555-013-2468<br>
    maelysbrant@snugwraps.example<br>
    snugwraps.example<br>
    348 Heron Mill Lane, Stamford, CT
  </div>
  <div class="wordmark"><span class="dot"></span>Snug Wraps</div>
  <div class="footer-band" role="img" aria-label="Dark footer band with multicolour wave decoration"></div>
  <div class="band-text">Vireltex fleece golf cart cushion covers<br>available with custom embroidery</div>
</section>

<section class="sheet envelope-back">
  <svg class="flap" viewBox="0 0 282 150" preserveAspectRatio="none">
    <path d="M0 0 L141 88 L282 0" stroke="#3a3a3d" stroke-width="1" fill="none"/>
    <path d="M0 150 L112 76 M282 150 L170 76" stroke="#3a3a3d" stroke-width="1" fill="none"/>
  </svg>
  <div class="wordmark"><span class="dot"></span>Snug Wraps</div>
</section>

<section class="sheet envelope-front">
  <div class="wordmark"><span class="dot"></span>Snug Wraps</div>
  <div class="return">348 Heron Mill Lane<br>Stamford, CT</div>
  <div class="footer-band" role="img" aria-label="Dark footer band with multicolour wave decoration"></div>
  <div class="band-text">Vireltex fleece golf cart cushion covers<br>available with custom embroidery</div>
</section>

<section class="sheet letterhead">
  <div class="wordmark"><span class="dot"></span>Snug Wraps</div>
  <div class="letter-body">
    <p>Dear Customer,</p>
    <p>Thank you for choosing our fleece cushion covers for your cart. Each cover is cut, sewn and finished by hand so it fits snugly and stays bright season after season.</p>
    <p>Our soft Vireltex fleece is warm in the morning and cool by noon. Choose from a wide range of colours, then add a name or club crest with custom embroidery.</p>
    <p>Every order is made in the USA and shipped within two weeks. We look forward to seeing you out on the course.</p>
    <p>Kind regards,<br><strong>Maelys Brant</strong></p>
  </div>
  <div class="footer-band" role="img" aria-label="Dark footer band with multicolour wave decoration"></div>
  <div class="band-text">Vireltex fleece golf cart cushion covers<br>available with custom embroidery</div>
  <div class="band-text-right">555-013-2468<br>snugwraps.example</div>
</section>

<section class="sheet fax-sheet">
  <div class="wordmark"><span class="dot"></span>Snug Wraps</div>
  <div class="fax-title">FAX</div>
  <div class="fax-fields">
    <div class="fax-field">To<span></span></div>
    <div class="fax-field">From<span></span></div>
    <div class="fax-field">Phone<span></span></div>
    <div class="fax-field">Fax<span></span></div>
    <div class="fax-field">Date<span></span></div>
    <div class="fax-field">Pages<span></span></div>
  </div>
  <div class="fax-checks">
    <label><i></i>Urgent</label>
    <label><i></i>For Review</label>
    <label><i></i>Please Comment</label>
    <label><i></i>Please Reply</label>
  </div>
  <div class="fax-comments">Comments</div>
  <div class="footer-band" role="img" aria-label="Dark footer band with multicolour wave decoration"></div>
  <div class="band-text">Vireltex fleece golf cart cushion covers<br>available with custom embroidery</div>
  <div class="band-text-right">555-013-2468<br>maelysbrant@snugwraps.example</div>
</section>

</body>
</html>
```